Web Design Project

Full website, similar _function_ to http://www.kindlarkfund.com/
You can not only make charities, but also communicate social or environmental problems by posting them on the website.
I need a full layout design, right now I am using a slightly changed bootstrap. View attached file "basic css" for current containers layout
Including front page, static text page (SEO), show listing page and content page, all the same look and feel. Dont focus to hard on the charity part...

Logo will be needed:
The URL - also the Logo - is Wutbrand.de - that is German for "Outcry" - so working with a "!" makes prob. sense, like Wutbrand!de or so... (EXTRA)

Colour Scheme:
I do not have a colour scheme, but I alreay think "Red URL with green elements" would be nice - that means please give me some other ideas ... I am not a designer, right?! :)

NO CODING NEEDED

Reason: I just got too few designs, some nice with it, though - I will clarify my needs new so it will be easier to reply with suggestions! :)

Target Market(s)

People who want to do charity and help other people

Industry/Entity Type

Charity

Requirements
Must have
• responsive design (tablet, smartphone)
static frame header (like here at pixelhive)

```html
<!DOCTYPE html>
<html lang="en">
<head>
<meta charset="utf-8">
<title>Company fundraising</title>
<link href="https://fonts.googleapis.com/css2?family=PT+Sans:wght@400;700&family=Roboto+Condensed:wght@400;700&family=Roboto+Slab:wght@300&display=swap" rel="stylesheet">
<style>
:root{
  --page:#f8eaea;
  --top:#3a0e0f;
  --red:#a9302f;
  --red-dark:#8a2223;
  --red-active:#c4504c;
  --accent:#e4615b;
  --green:#2e6d2f;
  --green-dark:#1f4f21;
  --green-light:#5aa153;
  --link-green:#2f7a2a;
  --text:#2b2222;
  --white:#ffffff;
  --foot:#8c2022;
  --foot-dark:#4b1011;
  --foot-link:#5e1213;
  --foot-head:#f1d5d3;
}
*{margin:0;padding:0;box-sizing:border-box}
html,body{width:923px;height:1200px;overflow:hidden}
body{position:relative;background:var(--page);font-family:"PT Sans",sans-serif;color:var(--text)}
.abs{position:absolute}

.topbar{left:0;top:0;width:923px;height:24px;background:var(--top)}
.topbar .home{left:134px;top:4px}
.topbar .account{right:58px;top:5px;font-size:11px;color:var(--accent)}
.topbar .account span{margin:0 5px;color:#9a4a48}

.header{left:0;top:24px;width:923px;height:56px;background:linear-gradient(#b63a37,var(--red) 60%,var(--red-dark));box-shadow:0 2px 4px rgba(0,0,0,.25)}
.logo{left:136px;top:6px;font-family:"Roboto Slab",serif;font-weight:300;font-size:40px;color:var(--white);letter-spacing:1px}
.mainnav{left:290px;top:0;height:56px;display:flex}
.mainnav a{display:block;height:56px;line-height:56px;padding:0 10px;font-size:13px;font-weight:700;color:var(--white);text-decoration:none;border-left:1px solid rgba(0,0,0,.15)}
.mainnav a:first-child{border-left:none}
.mainnav a.active{background:var(--red-active);color:#4a0c0c}

.subnav{left:79px;top:80px;width:755px;height:53px}
.subnav .item{position:absolute;top:0;height:53px;line-height:53px;font-size:12.5px;font-weight:700;color:var(--white);text-align:center}

.hero{left:78px;top:152px;width:756px;height:375px;background:var(--white);box-shadow:0 0 6px rgba(0,0,0,.2)}
.hero .photo{position:absolute;left:6px;top:6px;width:744px;height:363px;background:linear-gradient(90deg,#b48a82 0%,#8e5f57 40%,#a8786f 70%,#c8a39c 100%)}
.hero .caption{position:absolute;left:44px;top:262px;width:237px;height:92px;border-radius:8px;background:rgba(38,70,30,.8);color:var(--white);padding:8px 12px}
.caption p{font-size:14px;line-height:24px;white-space:nowrap}
.caption b{font-size:17px}
.caption a{display:block;text-align:right;margin-top:1px;font-size:14px;font-weight:700;color:#8cd14d}
.dots{left:416px;top:515px;width:82px;height:22px;background:var(--white);border-radius:0 0 10px 10px;box-shadow:0 2px 3px rgba(0,0,0,.2);display:flex;justify-content:center;align-items:center;gap:5px}
.dots i{width:11px;height:11px;border-radius:50%;background:#e6e6e6;border:1px solid #bbb}

.teaser{left:77px;top:559px;width:756px;height:153px;background:var(--white);border-radius:5px;overflow:hidden}
.teaser .bar{height:34px;background:linear-gradient(var(--green),var(--green-dark));color:var(--white);font-size:14px}
.teaser .bar span{position:absolute;top:7px;display:flex;align-items:center;gap:7px}
.teaser .col{position:absolute;top:42px;width:342px;font-size:10.8px;line-height:14.7px}
.teaser .divider{position:absolute;left:376px;top:42px;height:104px;border-left:1px dashed #bbb}

.sidenav{left:78px;top:732px;width:188px}
.sidenav a{display:flex;align-items:center;gap:9px;height:29px;padding-left:11px;font-size:12.5px;color:var(--white);text-decoration:none;background:linear-gradient(#3d8a3a,var(--green));border-bottom:1px solid #1c4a1e}
.sidenav a.active{background:linear-gradient(#2f7a2d,var(--green-dark))}
.sidenav .sub{display:flex;align-items:center;height:28px;padding-left:20px;gap:8px;font-size:11.5px;background:var(--white);border-bottom:1px solid #e6e0e0;border-left:1px solid #ddd;border-right:1px solid #ddd}
.sidenav .sub::before{content:"";border-left:4px solid var(--green);border-top:3px solid transparent;border-bottom:3px solid transparent}
.sidenav svg{width:12px;height:12px;fill:var(--white)}

.section-title{font-family:"Roboto Condensed",sans-serif;font-weight:700;font-size:14.5px;color:var(--green);text-decoration:underline}
.thumb{background:linear-gradient(135deg,#c9b7a8,#8a7a70);border:1px solid #666}
.thumb.pink{background:linear-gradient(135deg,#f3c6b4,#e07a6a);border-color:#b13}
.avatar{background:linear-gradient(#d9d4d0,#7c7673);border:1px solid #777}
.copy{font-size:11px;line-height:14.8px}
.copy.small{font-family:"Roboto Condensed",sans-serif;font-size:8.8px;line-height:14px}
.date{font-size:11px;font-style:italic;color:var(--link-green);text-decoration:underline}

.footer{left:0;top:1019px;width:923px;height:136px;background:var(--foot)}
.footer h4{position:absolute;top:18px;font-weight:400;font-size:13px;color:var(--foot-head)}
.footer ul{position:absolute;top:42px;list-style:none}
.footer li{height:24px;line-height:24px;font-size:11px;color:var(--foot-link);border-bottom:1px solid rgba(0,0,0,.15)}
.footer .label{position:absolute;font-size:12px;color:var(--foot-head)}
.subscribe{left:619px;top:41px;width:186px;height:27px;background:var(--white);border-radius:3px;display:flex;overflow:hidden}
.subscribe span{flex:1;font-size:11px;line-height:27px;padding-left:8px;color:#333}
.subscribe b{width:38px;background:linear-gradient(#5fb64a,#2f8a2b);display:flex;align-items:center;justify-content:center}
.social{left:618px;top:102px;display:flex;gap:11px}
.social i{width:24px;height:24px;border-radius:50%;background:#3e3e3e;border:1px solid #222}
.social i:nth-child(1){background:#2a72a6}
.social i:nth-child(2){background:#4b4b4b}
.social i:nth-child(3){background:#2e5fc8}
.social i:nth-child(5){background:#3a93c6}
.bottom{left:0;top:1155px;width:923px;height:45px;background:var(--foot-dark);text-align:center;line-height:45px;font-size:10px;color:var(--foot-head)}
</style>
</head>
<body>

<div class="abs topbar">
  <svg class="abs home" width="16" height="14" viewBox="0 0 16 14"><path d="M8 0 0 7h2v7h4V9h4v5h4V7h2z" fill="#e4615b"/></svg>
  <div class="abs account">Your account<span>|</span>Select Language ▾</div>
</div>

<header class="abs header">
  <div class="abs logo">LOGO</div>
  <nav class="abs mainnav">
    <a href="#">How it works</a>
    <a href="#">Charity membership</a>
    <a href="#" class="active">Company fundraising</a>
    <a href="#">Pertnership</a>
    <a href="#">Contacts</a>
    <a href="#">Help</a>
  </nav>
</header>

<nav class="abs subnav">
  <svg width="755" height="53" viewBox="0 0 755 53" style="position:absolute;left:0;top:0">
    <defs>
      <linearGradient id="barG" x1="0" y1="0" x2="0" y2="1"><stop offset="0" stop-color="#4e7e4c"/><stop offset="1" stop-color="#234a25"/></linearGradient>
      <linearGradient id="actG" x1="0" y1="0" x2="0" y2="1"><stop offset="0" stop-color="#8fd38a"/><stop offset="1" stop-color="#3f9a3f"/></linearGradient>
    </defs>
    <rect width="755" height="53" fill="url(#barG)"/>
    <polygon points="156,0 255,0 270,26.5 255,53 156,53 171,26.5" fill="url(#actG)"/>
    <g fill="none" stroke="#1a3a1b" stroke-width="1.5">
      <polyline points="156,0 171,26.5 156,53"/>
      <polyline points="255,0 270,26.5 255,53"/>
      <polyline points="354,0 369,26.5 354,53"/>
      <polyline points="453,0 468,26.5 453,53"/>
      <polyline points="547,0 562,26.5 547,53"/>
      <polyline points="641,0 656,26.5 641,53"/>
    </g>
  </svg>
  <span class="item" style="left:0;width:160px">Company fundraising</span>
  <span class="item" style="left:171px;width:92px;color:#173d18">Submenu 1</span>
  <span class="item" style="left:270px;width:92px">Submenu 2</span>
  <span class="item" style="left:369px;width:92px">Submenu 3</span>
  <span class="item" style="left:468px;width:87px">Submenu 4</span>
  <span class="item" style="left:562px;width:87px">Submenu 5</span>
  <span class="item" style="left:656px;width:92px">Submenu 6</span>
</nav>

<section class="abs hero">
  <div class="photo" role="img" aria-label="Photo of a school class standing in front of earthquake rubble, with a smiling child in the foreground"></div>
  <div class="caption">
    <p><b>DONATE</b> not only save their life,<br>also give them <b>JUSTICE...</b></p>
    <a href="#">Know more &gt;&gt;</a>
  </div>
</section>
<div class="abs dots"><i></i><i></i><i></i><i></i></div>

<section class="abs teaser">
  <div class="bar">
    <span style="left:19px">Teaser Panel <svg width="20" height="18" viewBox="0 0 20 18"><rect x="1" y="4" width="13" height="13" fill="none" stroke="#fff" stroke-width="1.6"/><path d="M4 9l4 4 10-12" fill="none" stroke="#fff" stroke-width="2.4"/></svg></span>
    <span style="left:399px">Teaser Panel <svg width="20" height="18" viewBox="0 0 20 18"><rect x="1" y="4" width="13" height="13" fill="none" stroke="#fff" stroke-width="1.6"/><path d="M4 9l4 4 10-12" fill="none" stroke="#fff" stroke-width="2.4"/></svg></span>
  </div>
  <p class="col" style="left:16px">Lorem ipsum dolor sit amet, consectetur adipisicing elit, sed do eiusmod tempor incididunt ut labore et dolore magna aliqua. Ut enim ad minim veniam, quis nostrud exercitation ullamco laboris nisi ut aliquip ex ea commodo consequat. Duis aute irure dolor in reprehenderit in voluptate velit esse cillum dolore eu fugiat nulla pariatur. Excepteur sint occaecat cupidatat non proident, sunt in culpa qui officia deserunt mollit anim id est laborum.</p>
  <div class="divider"></div>
  <p class="col" style="left:396px">Lorem ipsum dolor sit amet, consectetur adipisicing elit, sed do eiusmod tempor incididunt ut labore et dolore magna aliqua. Ut enim ad minim veniam, quis nostrud exercitation ullamco laboris nisi ut aliquip ex ea commodo consequat. Duis aute irure dolor in reprehenderit in voluptate velit esse cillum dolore eu fugiat nulla pariatur. Excepteur sint occaecat cupidatat non proident, sunt in culpa qui officia deserunt mollit anim id est laborum.</p>
</section>

<nav class="abs sidenav">
  <a href="#"><svg viewBox="0 0 12 12"><circle cx="4" cy="3" r="2"/><circle cx="8.5" cy="4" r="1.6"/><path d="M0 11c0-3 2-5 4-5s4 2 4 5zM8 11c0-2 .5-3 .5-4 2 0 3.5 1.5 3.5 4z"/></svg>How it works</a>
  <a href="#"><svg viewBox="0 0 12 12"><path d="M1 0h10v12H1zM3 2v2h6V2zm0 3v2h6V5zm0 3v2h6V8z" fill-rule="evenodd"/></svg>Charity membership</a>
  <a href="#" class="active"><svg viewBox="0 0 12 12"><path d="M0 1h12v10H0zM1 2v7l3-3 2 2 2-3 3 4V2z" fill-rule="evenodd"/></svg>Company fundraising</a>
  <div class="sub">Submenu 1</div>
  <div class="sub">Submenu 2</div>
  <div class="sub">Submenu 3</div>
  <a href="#"><svg viewBox="0 0 12 12"><circle cx="6" cy="4" r="3.5"/><path d="M4.5 7h3l-1 5h-1z"/></svg>Pertnership</a>
  <a href="#"><svg viewBox="0 0 12 12"><circle cx="6" cy="2.5" r="2"/><path d="M2 5h8v4H8v3H4V9H2z"/></svg>Contact Us</a>
  <a href="#"><svg viewBox="0 0 12 12"><circle cx="6" cy="2.5" r="2"/><path d="M2 5h8v4H8v3H4V9H2z"/></svg>Help</a>
</nav>

<h3 class="abs section-title" style="left:287px;top:735px">Blogs goes&nbsp; here</h3>
<div class="abs thumb" style="left:290px;top:764px;width:103px;height:66px" role="img" aria-label="Photo of many hands stacked together"></div>
<p class="abs copy" style="left:405px;top:760px;width:145px">Lorem ipsum dolor sit amet, consectetur adipisicing elit, sed do eiusmod tempor incididunt ut labore.</p>
<div class="abs thumb pink" style="left:573px;top:764px;width:103px;height:66px" role="img" aria-label="Illustration of children playing together"></div>
<p class="abs copy small" style="left:689px;top:760px;width:140px">Lorem ipsum dolor sit amet, consectetur adipisicing elit, sed do eiusmod tempor incididunt ut labore.</p>

<h3 class="abs section-title" style="left:287px;top:847px">Popular on Chatterly</h3>
<h3 class="abs section-title" style="left:572px;top:847px">Popular on Chirpline</h3>

<div class="abs avatar" style="left:291px;top:876px;width:44px;height:53px" role="img" aria-label="Portrait photo of the post author"></div>
<p class="abs copy" style="left:347px;top:873px;width:190px">Lorem ipsum dolor sit amet, consectetur adipisicing elit, sed do eiusmod tempor.<br><span class="date">Jan 12, 2013, Mara D. L.</span></p>
<div class="abs avatar" style="left:291px;top:939px;width:44px;height:53px" role="img" aria-label="Portrait photo of the post author"></div>
<p class="abs copy" style="left:347px;top:936px;width:190px">Lorem ipsum dolor sit amet, consectetur adipisicing elit, sed do eiusmod tempor.<br><span class="date">Jan 12, 2013, Mara D. L.</span></p>

<div class="abs avatar" style="left:574px;top:876px;width:44px;height:53px" role="img" aria-label="Portrait photo of the post author"></div>
<p class="abs copy" style="left:632px;top:873px;width:190px">Lorem ipsum dolor sit amet, consectetur adipisicing elit, sed do eiusmod tempor.<br><span class="date">Jan 12, 2013, Mara D. L.</span></p>
<div class="abs avatar" style="left:574px;top:939px;width:44px;height:53px" role="img" aria-label="Portrait photo of the post author"></div>
<p class="abs copy" style="left:632px;top:936px;width:190px">Lorem ipsum dolor sit amet, consectetur adipisicing elit, sed do eiusmod tempor.<br><span class="date">Jan 12, 2013, Mara D. L.</span></p>

<footer class="abs footer">
  <h4 style="left:77px">How it works</h4>
  <ul style="left:77px;width:85px"><li>Headline 1</li><li>Headline 1</li><li>Headline 1</li></ul>
  <h4 style="left:177px">Charity membership</h4>
  <ul style="left:177px;width:120px"><li>Headline 1</li><li>Headline 1</li><li>Headline 1</li></ul>
  <h4 style="left:324px">Company fundraising</h4>
  <ul style="left:324px;width:130px"><li>Headline 1</li><li>Headline 1</li><li>Headline 1</li></ul>
  <h4 style="left:479px">Pertnership</h4>
  <ul style="left:479px;width:100px"><li>Headline 1</li><li>Headline 1</li><li>Headline 1</li></ul>
  <span class="label" style="left:619px;top:19px">Subscribe us :</span>
  <div class="abs subscribe"><span>Your email address</span><b><svg width="18" height="14" viewBox="0 0 18 14"><path d="M1 7l5 5L17 1" fill="none" stroke="#d9f5c9" stroke-width="2.5"/></svg></b></div>
  <span class="label" style="left:619px;top:80px">Follow us :</span>
  <div class="abs social"><i></i><i></i><i></i><i></i><i></i></div>
</footer>
<div class="abs bottom">Copyright @ 2013, Company name, All rights are reserved.</div>

</body>
</html>
```